INTERNATIONAL SPEAKING BUSINESS FOR WOMEN NEEDS A BROCHURE DESIGN

HEARTWARD CIRCLE IS AN INTERNATIONAL FEMALE NETWORK PROVIDING ITS MEMBERS THE UK'S NUMBER ONE RELATIONSHIP SEMINAR FOR WOMEN.
WE ARE ABOUT TO GO LIVE AGAIN AFTER 18 MONTHS AND ONE OF OUR OFFERINGS AT THIS LIVE EVENT, IS OUR CONNECTION GROWTH PROGRAMME - AND THIS IS WHERE YOU COME IN :)
IM LOOKING FOR AN ELEGANT, EASY AND WARM TO THE EYE BROCHURE WHICH CAPTURES SOME OF OUR BEST TESTIMONIALS AND CLIENTS. WE HAVE THE LOGO, THE IMAGES AND THE COPY . WE JUST NEED YOUR AMAZING CREATIVE TALENT AND SKILL TO PUT IT ALL TOGETHER TO LOOK ELEGANT AND PROFESSIONAL, YET WELCOMING AND INSPIRING.
OUR IDEAL CLIENT IS A SINGLE, SUCCESSFUL, PROFESSIONAL WOMAN WANTING TO FIND A SOLUTION TO HER RELATIONSHIP CHALLENGES. SHE WANTS TO LET GO OF HER FEARS OF PAST RELATIONSHIPS AND ALIGN WITH AN AMAZING RELATIONSHIP. OUR AIM WITH THE BROCHURE IS TO SHOW THEM WHAT WE DO, HOW WE DO IT AND HOW OUR EXISTING CLIENTS HAVE ALREADY DONE THIS.
THIS IS JUST ONE OF MANY CREATIVE WORKS NEEDED TO BE CARRIED OUT OVER THESE NEXT FEW WEEKS
SO WE ARE LOOKING FOR OUR IDEAL CREATIVE PARTNER ! HOPING TO FIND YOU HERE ;)
heartwardcircle-example.com
professional, successful women between 30 and 65 looking to resolve their relationship problems
Speaking Business/ Seminars / webinars/ Relationships Coaching for Women
- Similar to logo and website heartwardcircle-example.com

```html
<!DOCTYPE html>
<html lang="en">
<head>
<meta charset="utf-8">
<title>Heartward Circle – Connection Growth Programme</title>
<link href="https://fonts.googleapis.com/css2?family=Fira+Sans:wght@400;600;700&family=Source+Serif+4:opsz,wght@8..60,400;8..60,700&family=Zilla+Slab:wght@700&display=swap" rel="stylesheet">
<style>
  :root {
    --pink: #ee4266;
    --ink: #3d3d3d;
    --grey: #a7a8ab;
    --paper: #ffffff;
  }
  * { margin: 0; padding: 0; box-sizing: border-box; }
  html, body { width: 1200px; height: 856px; overflow: hidden; background: var(--paper); }
  .page { position: relative; width: 1200px; height: 856px; color: var(--ink);
    font-family: "Source Serif 4", Georgia, serif; font-size: 17.6px; line-height: 23.7px; }
  .col { position: absolute; }
  .col-about { left: 63px; top: 58px; width: 345px; }
  .col-offer { left: 433px; top: 58px; width: 345px; }
  .col-voices { left: 803px; top: 58px; width: 350px; }
  .kicker { font-family: "Fira Sans", sans-serif; font-size: 22px; line-height: 24px; font-weight: 400; }
  .title { font-family: "Fira Sans", sans-serif; font-size: 24px; line-height: 25px; font-weight: 700; color: var(--pink); }
  .section-head { margin-bottom: 18px; }
  .section-gap { margin-top: 26px; }
  .bullets { list-style: none; }
  .bullets li { position: relative; padding-left: 16px; }
  .bullets li::before { content: "•"; position: absolute; left: 2px; font-size: 13px; }
  .price { display: flex; align-items: center; margin: 22px 0 16px; }
  .price-amount { font-family: "Fira Sans", sans-serif; font-weight: 700; font-size: 62px; line-height: 56px; color: var(--pink); }
  .price-label { margin-left: 16px; font-family: "Fira Sans", sans-serif; font-size: 22px; line-height: 20px; }
  .price-label strong { font-weight: 600; display: block; }
  .included { margin-bottom: 2px; }
  .included em { font-style: normal; font-weight: 700; color: var(--pink); }
  .register { margin-top: 31px; }
  .heading-main { font-family: "Fira Sans", sans-serif; font-weight: 700; font-size: 25px; line-height: 28px; }
  .person-name { font-family: "Zilla Slab", serif; font-weight: 700; font-size: 16px; line-height: 20px; color: var(--pink); }
  .person-role { line-height: 23.7px; }
  .portrait { position: absolute; border-radius: 50%; }
  .portrait-one { left: 1037px; top: 105px; width: 113px; height: 113px; background: radial-gradient(circle at 45% 40%, #e8d6a8, #9a9c86 70%, #6f8a72); }
  .portrait-two { left: 803px; top: 397px; width: 115px; height: 115px; background: radial-gradient(circle at 50% 45%, #efd8c4, #b59c82 65%, #6d5e52); }
  .quote-one { position: absolute; left: 803px; top: 232px; width: 355px; }
  .meta-one { position: absolute; left: 803px; top: 129px; width: 220px; }
  .meta-two { position: absolute; left: 934px; top: 432px; width: 230px; }
  .quote-two { position: absolute; left: 803px; top: 525px; width: 355px; }
  .footer-arcs { position: absolute; left: 0; top: 810px; }
</style>
</head>
<body>
<div class="page">

  <section class="col col-about">
    <div class="section-head"><p class="kicker">About</p><h2 class="title">The Masterclass</h2></div>
    <p>Immerse yourself with a group of like minded individuals in a weekly masterclass and get absorbed in some of the most senior relationships content that’s changing the lives of thousands of women internationally.</p>
    <div class="section-head section-gap"><p class="kicker">What will I learn</p><h2 class="title">from the programme?</h2></div>
    <ul class="bullets">
      <li>Weekly opportunity to have all your burning relationship questions answered</li>
      <li>Immerse with a powerful network of like-minded women and learn even more</li>
      <li>Tools to help you overcome past relationship wounds and patterns</li>
      <li>Deepen your understanding of self-mastery on route to relationship Mastery</li>
    </ul>
  </section>

  <section class="col col-offer">
    <div class="section-head"><p class="kicker">Is this</p><h2 class="title">programme for me?</h2></div>
    <p>If you wish to join one of the UK’s Top Female Networks for a life changing year, then the Masterclass programme is for you. Give yourself that step in between the Connection Growth Programme Series.</p>
    <div class="price"><span class="price-amount">$200</span><span class="price-label"><strong>Subscription</strong>fee</span></div>
    <p class="included">Here’s <em>what’s included</em>:</p>
    <ul class="bullets">
      <li>Receive full access to the Connection Growth Programme (once a week)</li>
      <li>Gain full access to the network via our private MemberHub group</li>
    </ul>
    <p class="register">Register today and get the first months’ worth <strong>TODAY</strong>. Tomorrow, wake up and watch half a day of the most powerful content for relationships out there. That’s half a day of advanced content</p>
  </section>

  <section class="col col-voices">
    <h2 class="heading-main">Testimonials</h2>
  </section>

  <div class="meta-one"><p class="person-name">Leyla Marsh, 34</p><p class="person-role">Missing and exploitation coordinator.</p></div>
  <div class="portrait portrait-one" role="img" aria-label="Portrait photo of Leyla Marsh"></div>
  <p class="quote-one">I joined Heartward Circle to solve issues I had in my relationships with men that I had been carrying for a long time. This has been a life changing experience of which I am eternally grateful.</p>

  <div class="portrait portrait-two" role="img" aria-label="Portrait photo of Helen Dorsey"></div>
  <div class="meta-two"><p class="person-name">Helen Dorsey, 63</p><p class="person-role">Midwife Labor Ward</p></div>
  <p class="quote-two">“I honestly didn’t know how this was going to help me get through the pain of my marriage breakup. Then one evening something in the message landed. Clara was talking about recognising and letting the emotions burn through and that absolutely resonated with me.</p>

  <svg class="footer-arcs" width="1200" height="46" viewBox="0 0 1200 46" aria-hidden="true">
    <ellipse cx="385" cy="90" rx="325" ry="88" fill="var(--grey)"/>
    <ellipse cx="783" cy="96" rx="290" ry="94" fill="var(--pink)"/>
  </svg>
</div>
</body>
</html>
```